KELPO's Coffee Liqueur Shot Arabica

Need a lable for a 500ml bottle of homemade Coffee liqueur.
Name:
KELPO's
Coffee
Shot

Shape: Round, 80mm
Color of the lable should be black and letters in black.
Letters KELPO's min 12mm hight.
Color of the liqueur is dark brown.
Add: 500ml
Add: 38% vol.
Should have a bean on the lable.
Maybe some bullet words on the bottom...
Prefered design see Pic1a with bottle.

Target Market(s)

People that enjoy coffee in shots, in coctails, with ice or on top of icecream or any other dessert

Font styles to use
Serif

Colors

Designer to choose colors to be used in the design.

Requirements
Must have
• See Pic 1a
Nice to have
• See Pic1a (bottle)
Should not have
• Different colors

```html
<!DOCTYPE html>
<html lang="en">
<head>
<meta charset="utf-8">
<title>KELPO's Coffee Shot – Label</title>
<link href="https://fonts.googleapis.com/css2?family=Archivo+Black&family=Josefin+Sans:wght@600&family=Montserrat:wght@700&family=Kaushan+Script&display=swap" rel="stylesheet">
<style>
  :root {
    --backdrop: #f2f0ec;
    --label-paper: #ffffff;
    --ink: #2a2a2a;
    --ink-soft: #4a4a4a;
    --bean-ghost: #ececec;
    --label-edge: #d9d6d0;
  }
  html, body {
    margin: 0;
    padding: 0;
    width: 1200px;
    height: 1200px;
    overflow: hidden;
    background: var(--backdrop);
  }
  .label {
    display: block;
    width: 1200px;
    height: 1200px;
  }
  .label-disc { fill: var(--label-paper); stroke: var(--label-edge); stroke-width: 2; }
  .inner-ring { fill: none; stroke: var(--ink-soft); stroke-width: 4; }
  .brand-name {
    font-family: "Archivo Black", sans-serif;
    font-size: 118px;
    letter-spacing: 6px;
    fill: var(--ink);
  }
  .est-line {
    font-family: "Josefin Sans", sans-serif;
    font-weight: 600;
    font-size: 44px;
    letter-spacing: 4px;
    fill: var(--ink);
  }
  .product-title {
    font-family: "Archivo Black", sans-serif;
    font-size: 112px;
    fill: var(--ink);
  }
  .product-sub {
    font-family: "Kaushan Script", cursive;
    font-size: 140px;
    fill: var(--ink);
  }
  .spec {
    font-family: "Montserrat", sans-serif;
    font-weight: 700;
    font-size: 48px;
    fill: var(--ink);
  }
  .bullet-word {
    font-family: "Archivo Black", sans-serif;
    font-size: 68px;
    letter-spacing: 5px;
    fill: var(--ink);
  }
  .rule { stroke: var(--ink); stroke-width: 4; stroke-linecap: round; }
  .bean-ghost { fill: var(--bean-ghost); }
  .bean-icon { fill: var(--ink); }
  .bean-crease { fill: none; stroke: var(--label-paper); stroke-width: 5; stroke-linecap: round; }
</style>
</head>
<body>
<svg class="label" viewBox="0 0 1200 1200" xmlns="http://www.w3.org/2000/svg">
  <defs>
    <path id="arc-top" d="M 225,600 A 375 375 0 0 1 975,600"/>
    <path id="arc-bottom" d="M 190,600 A 410 410 0 0 0 1010,600"/>
  </defs>

  <circle class="label-disc" cx="600" cy="600" r="500"/>

  <g class="bean-backdrop" role="img" aria-label="Faint coffee beans decoration behind the title">
    <ellipse class="bean-ghost" cx="540" cy="690" rx="120" ry="190" transform="rotate(-25 540 690)"/>
    <ellipse class="bean-ghost" cx="690" cy="470" rx="110" ry="170" transform="rotate(25 690 470)"/>
  </g>

  <circle class="inner-ring" cx="600" cy="600" r="340"/>

  <text class="brand-name" text-anchor="middle">
    <textPath href="#arc-top" startOffset="50%">KELPO's</textPath>
  </text>

  <g class="est">
    <line class="rule" x1="430" y1="358" x2="455" y2="358"/>
    <text class="est-line" x="600" y="372" text-anchor="middle">EST.2025</text>
    <line class="rule" x1="745" y1="358" x2="770" y2="358"/>
  </g>

  <text class="product-title" x="600" y="650" text-anchor="middle" textLength="640" lengthAdjust="spacingAndGlyphs">COFFEE</text>

  <g class="product-subline">
    <line class="rule" x1="400" y1="772" x2="450" y2="772"/>
    <text class="product-sub" x="600" y="800" text-anchor="middle">Shot</text>
    <line class="rule" x1="750" y1="772" x2="800" y2="772"/>
  </g>

  <g class="spec-left">
    <text class="spec" x="160" y="550" text-anchor="middle">38%</text>
    <text class="spec" x="160" y="625" text-anchor="middle">VOL</text>
  </g>
  <g class="spec-right">
    <text class="spec" x="1040" y="550" text-anchor="middle">500</text>
    <text class="spec" x="1040" y="625" text-anchor="middle">ML</text>
  </g>

  <text class="bullet-word" text-anchor="middle">
    <textPath href="#arc-bottom" startOffset="29%">ARABICA</textPath>
  </text>
  <text class="bullet-word" text-anchor="middle">
    <textPath href="#arc-bottom" startOffset="71%">INTENSIV</textPath>
  </text>

  <g class="bean-mark" transform="translate(600 945)">
    <ellipse class="bean-icon" cx="-24" cy="4" rx="28" ry="42" transform="rotate(-20 -24 4)"/>
    <path class="bean-crease" d="M -34,-32 C -14,-10 -40,15 -16,40"/>
    <ellipse class="bean-icon" cx="26" cy="-2" rx="28" ry="42" transform="rotate(20 26 -2)"/>
    <path class="bean-crease" d="M 36,-38 C 14,-14 40,10 16,34"/>
  </g>
</svg>
</body>
</html>
```